Fernwick Digital Marketing Agency Website Design. I need a new website for my digital marketing agency. It needs to be FAST and easy to use. I want to be able to add videos to the main homepage like this page: https://www.lumatreeweb.example/search-marketing/cleveland-ohio-seo-companyI'd like to have the request quote tab on the top right side as well as my number above it. The following website is my favorite overall: http://www.vantorelgroup.example/ I'd love to copy something like that.

***** Website I want to copy: http://www.vantorelgroup.example/services/ ******
Updates

This needs to be a Wordpress website. Sorry for any confusion as this is the first time using MakerQuill. I need the homepage as described as well as a Services Page and Contact Us page. Services page should be simply yet creative with a spot for me to insert up to 8 services.

Target Market(s)

Business owners

Industry/Entity Type

Digital Marketing

Coding

Coded - Design and coding required

Number of Pages Required

3 page

Font styles to use
Other font styles liked:
• Oswald

Colors

Designer to choose colors to be used in the design.

Requirements
Must have
• I need to have a nice design/template to work off of in Wordpress. It needs to be bright and vibrant yet elegant in design.
Nice to have
• CTA at the top right as well as a place for the phone number. http://www.vantorelgroup.example/services/

```html
<!DOCTYPE html>
<html lang="en">
<head>
<meta charset="utf-8">
<title>Fernwick Digital Marketing Agency</title>
<link rel="stylesheet" href="https://fonts.googleapis.com/css2?family=Raleway:wght@500;600;700;800;900&family=Roboto:wght@400;500;700&display=swap">
<style>
:root{
  --orange:#ff7a18;
  --orange-deep:#f36b0c;
  --peach:#fde7d5;
  --peach-soft:#fff1e6;
  --dot-tone:#ffd9bd;
  --ink:#1f1f1f;
  --text:#333;
  --muted:#9a9a9a;
  --line:#555;
  --white:#fff;
}
*{box-sizing:border-box;margin:0;padding:0}
html,body{width:1200px;height:3273px;overflow:hidden}
body{position:relative;background:var(--white);font-family:"Roboto",sans-serif;color:var(--text)}
.abs{position:absolute}
a{color:inherit;text-decoration:none}

/* header */
.hero-blob{left:0;top:0}
.brand{left:96px;top:30px;color:var(--white);font-family:"Raleway",sans-serif;font-weight:700;display:flex;align-items:center;gap:12px}
.brand-mark{width:22px;height:22px;border-radius:50%;background:var(--white)}
.brand-name{font-size:30px;line-height:1;letter-spacing:1px}
.brand-sub{font-size:15px;line-height:1.2;margin-top:4px}
.phone{right:96px;top:26px;color:var(--orange);font-family:"Raleway",sans-serif;font-weight:600;font-size:26px;display:flex;align-items:center;gap:10px}
.nav{right:96px;top:74px;display:flex;align-items:center;gap:26px;font-size:15px;color:var(--orange)}
.nav .active{border:1.5px solid var(--orange);padding:3px 12px}
.nav .quote{background:var(--orange);color:var(--white);font-weight:700;padding:5px 12px;border-radius:3px}

.hero-media{left:168px;top:160px;width:572px;height:406px;border-radius:14px;background:linear-gradient(160deg,#6b6b6b,#a59a90 55%,#e8e8e8)}
.grow{right:96px;top:158px;font-family:"Raleway",sans-serif;font-weight:800;font-size:104px;color:var(--orange);letter-spacing:2px;line-height:1}
.tagline{right:96px;top:300px;text-align:right;font-family:"Raleway",sans-serif;font-weight:700;font-size:23px;line-height:44px;color:var(--ink)}
.cta{right:96px;top:451px;width:230px;height:40px;background:var(--orange);color:var(--white);font-weight:700;font-size:17px;display:flex;align-items:center;justify-content:center;border-radius:2px}

/* section headings */
.heading{font-family:"Raleway",sans-serif;font-weight:700;font-size:31px;color:var(--ink);line-height:1}
.heading::after{content:"";display:block;width:64px;height:3px;background:var(--orange);margin-top:10px}
.heading.center{text-align:center;width:100%;left:0}
.heading.center::after{margin:10px auto 0}

/* about */
.about-title{left:98px;top:757px}
.about-lead{left:98px;top:808px;width:560px;font-weight:500;font-size:18px;line-height:44px;color:var(--ink)}
.about-copy{left:98px;top:896px;width:560px;font-size:18px;line-height:44px;color:var(--muted)}
.about-photo{left:709px;top:742px}

/* services */
.services-bg{left:0;top:1250px}
.services-title{top:1240px}
.dot-field{left:872px;top:1288px;width:272px;height:310px;background:var(--dot-tone);opacity:.7}
.card{top:1342px;width:279px;height:333px;background:var(--white);box-shadow:0 6px 24px rgba(0,0,0,.08);text-align:center;padding:26px 28px 0}
.card-icon{width:110px;height:100px;margin:0 auto;border-radius:12px;background:linear-gradient(135deg,var(--orange),#ffb27a)}
.card h3{font-family:"Raleway",sans-serif;font-weight:600;font-size:19px;color:var(--ink);margin-top:42px}
.card p{font-size:11.5px;line-height:18px;color:#666;margin-top:14px}
.card .more{position:absolute;left:0;right:0;bottom:30px;font-weight:700;font-size:15px;color:#444;text-decoration:underline}
.pager{left:536px;top:1722px;display:flex;align-items:center;gap:22px}
.pager span{width:7px;height:7px;border-radius:50%;border:1px solid var(--orange)}
.pager span.on{background:var(--orange)}
.pager i{display:block;width:16px;height:1px;background:#f0b98a;margin:0 -19px}

/* grow section */
.grow-illus{left:76px;top:1876px;width:520px;height:280px;border-radius:46% 54% 48% 52% / 40% 38% 62% 60%;background:linear-gradient(135deg,var(--peach-soft),#ffb27a 60%,var(--orange))}
.grow-title{right:96px;top:1844px;text-align:right;font-family:"Raleway",sans-serif;font-weight:700;font-size:24px;line-height:44px;color:var(--ink)}
.grow-copy{right:96px;top:1942px;width:500px;text-align:right;font-size:16px;line-height:44px;color:var(--muted)}

/* contact */
.contact-title{top:2236px}
.field{left:94px;width:480px;border-bottom:1.5px solid var(--line);font-weight:700;font-size:18px;color:var(--ink)}
.send{left:94px;top:2690px;width:131px;height:29px;border-radius:15px;background:var(--orange);color:var(--white);font-weight:700;font-size:14px;display:flex;align-items:center;justify-content:center;box-shadow:0 6px 14px rgba(255,122,24,.35)}
.map{left:657px;top:2352px;width:464px;height:367px;background:linear-gradient(135deg,#dfe6d8,#eceae4 50%,#d9e4d0)}

/* footer */
.footer-bg{left:0;top:2820px}
.subscribe{left:94px;top:2900px;width:1078px;height:76px;border-radius:38px;background:var(--orange);box-shadow:0 8px 20px rgba(255,122,24,.3)}
.subscribe h4{left:118px;top:24px;font-family:"Raleway",sans-serif;font-weight:700;font-size:22px;color:var(--white)}
.subscribe .email{left:469px;top:21px;width:276px;height:34px;border-radius:17px;background:var(--white);font-size:10px;color:#bbb;padding:11px 20px}
.subscribe .go{left:818px;top:21px;width:109px;height:34px;border-radius:17px;border:2px solid var(--white);color:var(--white);font-weight:700;font-size:17px;display:flex;align-items:center;justify-content:center}
.foot-brand{left:94px;top:3020px;color:var(--orange);font-family:"Raleway",sans-serif;font-weight:700}
.foot-brand .brand-mark{background:var(--orange)}
.foot-about{left:94px;top:3126px;width:240px;font-size:11px;line-height:19px;color:#555}
.foot-col{top:3020px}
.foot-col h5{font-size:13px;font-weight:700;color:var(--orange);margin-bottom:12px}
.foot-col li{list-style:none;font-size:14px;line-height:30px;color:#555}
.copyright{left:0;width:100%;top:3237px;text-align:center;font-size:11px;color:#555}
</style>
</head>
<body>

<svg class="abs hero-blob" width="760" height="600" viewBox="0 0 760 600" aria-hidden="true">
  <path d="M0 0H452C495 90 560 220 650 330C700 390 735 440 745 500C640 540 470 560 330 550C190 540 70 505 0 450Z" fill="var(--orange)"/>
</svg>

<div class="abs brand">
  <span class="brand-mark"></span>
  <div><div class="brand-name">Fernwick</div><div class="brand-sub">Digital Marketing Agency</div></div>
</div>

<div class="abs phone">
  <svg width="20" height="20" viewBox="0 0 24 24" aria-hidden="true"><path fill="var(--orange)" d="M6.6 10.8a15.1 15.1 0 0 0 6.6 6.6l2.2-2.2c.3-.3.7-.4 1-.2 1.1.4 2.3.6 3.6.6.6 0 1 .4 1 1V20c0 .6-.4 1-1 1A17 17 0 0 1 3 4c0-.6.4-1 1-1h3.5c.6 0 1 .4 1 1 0 1.3.2 2.5.6 3.6.1.3 0 .7-.2 1z"/></svg>
  +1 555-014-2290
</div>
<nav class="abs nav">
  <a class="active">Home</a><a>Services</a><a>Blog</a><a>Contact Us</a><a>FAQ</a><a class="quote">Request Quote</a>
</nav>

<div class="abs hero-media" role="img" aria-label="Desktop computer with keyboard and mouse playing the agency promo video"></div>

<div class="abs grow">GROW</div>
<div class="abs tagline">This Is All About Your Company<br>Growing Online.<br>End Of Story.</div>
<a class="abs cta">Grow my company now</a>

<h2 class="abs heading about-title">ABOUT US</h2>
<p class="abs about-lead">Seo Company In Cleveland, Ohio - Search Engine Optimization Services For Local Businesses In Ohio</p>
<p class="abs about-copy">Sed ut perspiciatis unde omnis iste natus error sit voluptatem accusantium doloremque laudantium, totam rem aperiam, eaque ipsa quae ab illo inventore veritatis et quasi architecto beatae vitae dicta sunt explicabo. Nemo enim ipsam voluptatem quia voluptas sit aspernatur aut odit aut fugit, sed quia consequuntur</p>
<svg class="abs about-photo" width="394" height="414" viewBox="0 0 394 414" role="img" aria-label="Man in a red sweater tapping a digital interface on a city street">
  <defs><linearGradient id="aboutFill" x1="0" y1="0" x2="1" y2="1"><stop offset="0" stop-color="#c9ccd0"/><stop offset=".55" stop-color="#8a6a66"/><stop offset="1" stop-color="#5b4a4a"/></linearGradient></defs>
  <path d="M150 20C200 0 260 30 300 60C360 100 394 170 390 250C386 340 320 410 230 414C150 418 90 370 70 300C60 260 40 240 10 220C-10 190 20 150 60 130C100 110 110 40 150 20Z" fill="url(#aboutFill)"/>
</svg>

<svg class="abs services-bg" width="1200" height="520" viewBox="0 0 1200 520" aria-hidden="true">
  <path d="M0 40C80 0 180 10 230 80C270 140 250 200 320 220C420 250 700 220 860 300C960 350 960 470 860 505C760 540 560 510 420 500C260 490 90 500 0 470Z" fill="var(--peach)"/>
</svg>
<h2 class="abs heading center services-title">OUR SERVICES</h2>
<div class="abs dot-field" role="img" aria-label="Decorative dot pattern"></div>

<article class="abs card" style="left:133px">
  <div class="card-icon" role="img" aria-label="Search optimization icon with monitor and chart"></div>
  <h3>Search Optimization</h3>
  <p>Whether it's On-Page, Off-Page, Local Citations, or straight up Searchly Business Page enhancements.</p>
  <a class="more">Read more</a>
</article>
<article class="abs card" style="left:458px">
  <div class="card-icon" role="img" aria-label="Code window icon with gear"></div>
  <h3>Social Media Marketing</h3>
  <p>Let's face it, your company needs a social media presence in today's world. It's no longer a desire.</p>
  <a class="more">Read more</a>
</article>
<article class="abs card" style="left:781px">
  <div class="card-icon" role="img" aria-label="Search ads service icon"></div>
  <h3>Searchly Ads</h3>
  <p>Do you want to take up more space on the real estate of Searchly? Are you ready for the increase in customer calls and transactions?</p>
  <a class="more">Read more</a>
</article>
<div class="abs pager"><span class="on"></span><i></i><span></span><i></i><span></span><i></i><span></span><i></i><span></span></div>

<div class="abs grow-illus" role="img" aria-label="Illustration of a marketer working at a wall of orange monitors"></div>
<h2 class="abs grow-title">Are You Ready To Grow Your Company's<br>Revenue With Digital Marketing?</h2>
<p class="abs grow-copy">Sed ut perspiciatis unde omnis iste natus error sit voluptatem accusantium doloremque laudantium, totam rem aperiam, eaque ipsa quae ab illo inventore veritatis et quasi architecto beatae vitae dicta sunt explicabo. Nemo enim ipsam voluptatem quia voluptas sit aspernatur aut odit aut fugit, sed q</p>

<h2 class="abs heading center contact-title">CONTACT US</h2>
<div class="abs field" style="top:2352px;height:28px">Name</div>
<div class="abs field" style="top:2439px;height:28px">Email</div>
<div class="abs field" style="top:2526px;height:117px">Message</div>
<a class="abs send">SEND</a>
<div class="abs map" role="img" aria-label="Street map showing the office location"></div>

<svg class="abs footer-bg" width="1200" height="453" viewBox="0 0 1200 453" aria-hidden="true">
  <path d="M0 200C200 150 420 190 640 150C860 110 1040 60 1200 0V453H0Z" fill="var(--peach)"/>
</svg>
<div class="abs subscribe">
  <h4 class="abs">Subscribe to Happy Hour!</h4>
  <div class="abs email">Enter your email address</div>
  <a class="abs go">SEND</a>
</div>

<div class="abs brand foot-brand">
  <span class="brand-mark"></span>
  <div><div class="brand-name">Fernwick</div><div class="brand-sub">Digital Marketing Agency</div></div>
</div>
<p class="abs foot-about">There are many variations of passages of Lorem Ipsum available, but the majority have suffered alteration in some form, by injected humour,</p>

<div class="abs foot-col" style="left:445px"><h5>QUICK LINKS</h5><ul><li>Home</li><li>About us</li><li>Services</li><li>Contact us</li></ul></div>
<div class="abs foot-col" style="left:711px"><h5>SERVICES</h5><ul><li>Content Marketing</li><li>Search Optimization</li><li>Social Media</li><li>Email Marketing</li></ul></div>
<div class="abs foot-col" style="left:1025px"><h5>FOLLOW US</h5><ul><li>Friendlane</li><li>Snapgrid</li><li>Chirpline</li><li>Workhub</li></ul></div>

<p class="abs copyright">Copyrights 2019. All rights reserved</p>

</body>
</html>
```